Business IT Services Billboard to attract local small businesses

We are Brivolux, a premier Managed Service Provider (MSP) specializing in comprehensive IT services and VOIP phone solutions exclusively for businesses. Our goal is to create a dynamic and visually engaging billboard advertisement that not only highlights our cutting-edge IT solutions but also emphasizes our state-of-the-art VOIP phone services. This billboard should communicate our commitment to providing innovative, reliable, and holistic technology solutions.
Target Market(s)
small business
Industry/Entity Type
Information Technology
Colors
Designer to choose colors to be used in the design.
Look and feel
Each slider illustrates characteristics of the customer's brand and the style your logo design should communicate.

```html
<!DOCTYPE html>
<html lang="en">
<head>
<meta charset="utf-8">
<title>Brivolux Billboard</title>
<link href="https://fonts.googleapis.com/css2?family=Open+Sans:wght@300;400;700;800&family=Roboto:wght@400&family=Roboto+Condensed:wght@500&display=swap" rel="stylesheet">
<style>
  :root {
    --page-bg: #e4e4e4;
    --navy-deep: #08162e;
    --navy-mid: #12305c;
    --navy-glow: #1d4f8f;
    --suit-dark: #161d2a;
    --suit-mid: #2a3342;
    --shirt: #c9d2de;
    --white: #ffffff;
    --brand-blue: #0b63b5;
    --ink: #1f2a36;
  }
  * { box-sizing: border-box; margin: 0; padding: 0; }
  html, body { width: 1071px; height: 1200px; overflow: hidden; background: var(--page-bg); }
  .billboard {
    position: absolute; left: 30px; top: 378px; width: 1011px; height: 443px;
    background: radial-gradient(ellipse at 30% 40%, var(--navy-glow) 0%, var(--navy-mid) 40%, var(--navy-deep) 100%);
    overflow: hidden;
    box-shadow: 0 10px 18px rgba(0,0,0,0.18);
  }
  .portrait {
    position: absolute; right: 0; top: 0; width: 446px; height: 371px;
    background: linear-gradient(100deg, rgba(8,22,46,0) 0%, var(--suit-dark) 28%, var(--suit-mid) 50%, var(--shirt) 62%, var(--suit-mid) 72%, var(--suit-dark) 100%);
  }
  .headline {
    position: absolute; left: 40px; top: 22px;
    font-family: "Open Sans", sans-serif; font-weight: 300; font-size: 61px; line-height: 55px;
    color: var(--white); letter-spacing: -0.5px; white-space: nowrap;
  }
  .headline strong { font-weight: 700; }
  .subline {
    position: absolute; left: 40px; top: 228px;
    font-family: "Open Sans", sans-serif; font-weight: 400; font-size: 31px; line-height: 41px;
    color: var(--white); white-space: nowrap;
  }
  .footer {
    position: absolute; left: 0; top: 371px; width: 1011px; height: 60px; background: var(--white);
    display: flex; align-items: center; justify-content: space-between; padding: 0 37px 0 39px;
  }
  .brand-name {
    font-family: "Open Sans", sans-serif; font-weight: 800; font-size: 40px; color: var(--brand-blue);
    letter-spacing: 7px; text-transform: uppercase; line-height: 1;
  }
  .call-to-action { font-family: "Roboto", sans-serif; font-size: 18px; color: var(--ink); white-space: nowrap; }
  .call-to-action .url { font-family: "Roboto Condensed", sans-serif; font-weight: 500; font-size: 29px; color: var(--brand-blue); margin-left: 4px; }
  .base-strip { position: absolute; left: 0; top: 431px; width: 1011px; height: 12px; background: linear-gradient(90deg, var(--navy-deep), var(--navy-mid)); }
</style>
</head>
<body>
  <section class="billboard">
    <div class="portrait" role="img" aria-label="Photo of a businessman in a dark suit and tie touching a floating cluster of hexagon service icons"></div>

    <h1 class="headline">Elevate Your Business<br>with <strong>Next-Gen IT</strong> and<br><strong>VOIP Services</strong></h1>
    <p class="subline">Innovative&nbsp; IT and VOIP Solutions<br>Tailored for Your Business Success.</p>

    <footer class="footer">
      <span class="brand-name">Brivolux</span>
      <p class="call-to-action">Transform Your Tech Today at <span class="url">www.brivolux.com</span></p>
    </footer>
    <div class="base-strip"></div>
  </section>
</body>
</html>
```